Brandt WordPress Design Contest

We need a wordpress design that will incorporate a professional color scheme with company logo in a clean layout. The design needs to consider that this will be developed on a responsive theme. Colors are up to the designer - The green of the logo with black, gray or an accent color. Client wants a 'modern' look.

Industry/Entity Type

It Company

Number of Pages Required

1 page

Font styles to use
Serif
Sans Serif

Requirements
Must have
• Navigation: 1) Home 2) All Auctions 3) Real Estate for Sale 4) Services 5) About Us 6) Contact Us
• Colors - a corporate look with professional color scheme. Green of logo + black and gray, or an eggshell/light beige, or any other accent that keeps within a corporate look.
• In header - logo (attached) , and contact info :5127 Old Harrow Lane, Scottsville, KY 42179
• 270-555-3946
• Fax: 270-555-3947
• Email:info@brandtpropertybidhouse.example
• Design will feature a full width (960 px) slideshow - use a stock photo for real estate.
• Widgets in sidebar or where appropriate - 1) Email Signup 2) Message of the Day 3) Upcoming Auctions 4) News&Events blog 5) Testimonials 6) Social media - FB, twitter, youtube, pinterest, google+
• Footer will have company logo, association logos (attached) and contact info, with another widget area if necessary
Nice to have
• use of drop down menu styling - Upcoming Auctions / Online Auctions/ Past Auctions under the "Auction Calendar" menu item

```html
<!DOCTYPE html>
<html lang="en">
<head>
<meta charset="utf-8">
<title>Brandt Property Bid House</title>
<link href="https://fonts.googleapis.com/css2?family=Montserrat:wght@600;700&family=Roboto:wght@400&display=swap" rel="stylesheet">
<style>
:root{
  --green:#0b6229;
  --green-line:#0d6a2c;
  --white:#ffffff;
  --panel:#eeefee;
  --ink:#1d1d1d;
}
*{box-sizing:border-box;margin:0;padding:0}
html,body{width:838px;height:1200px;overflow:hidden;background:var(--white)}
body{position:relative;font-family:"Roboto",Arial,sans-serif;color:var(--white)}
.hero{position:absolute;left:0;top:0;width:838px;height:522px;
  background:linear-gradient(180deg,#4a4a4a 0%,#8fa3ae 28%,#5f86a3 45%,#6d7a5a 60%,#3a3c3a 78%,#2a2d2f 100%)}
.hero-arrow{position:absolute;top:304px;width:16px;height:28px}
.hero-arrow.prev{left:26px}.hero-arrow.next{right:26px}
.top-info{position:absolute;right:27px;top:22px;font-size:7px;letter-spacing:.2px;display:flex;gap:9px}
.brand{position:absolute;display:flex;flex-direction:column;align-items:center;justify-content:center;
  width:102px;height:68px;background:var(--white);border:2px solid var(--green);color:var(--green)}
.brand .name{font-family:"Montserrat",sans-serif;font-weight:700;font-size:22px;line-height:1;display:flex;align-items:center;gap:5px}
.brand .mark{width:9px;height:9px;background:var(--green)}
.brand .phone{font-family:"Montserrat",sans-serif;font-weight:700;font-size:10px;margin-top:5px}
.header .brand{left:29px;top:21px}
.nav{position:absolute;top:63px;left:0;height:25px;font-size:11px;letter-spacing:.2px}
.nav a{position:absolute;top:6px;color:var(--white);text-decoration:none;white-space:nowrap}
.nav .active{top:0;left:212px;width:93px;height:25px;border:1.5px solid rgba(255,255,255,.75);
  display:flex;align-items:center;justify-content:center}
.dropdown{position:absolute;left:212px;top:88px;width:93px}
.dropdown a{display:flex;align-items:center;justify-content:center;height:27px;
  border:1px solid rgba(255,255,255,.6);border-top:none;font-size:7px;color:var(--white);text-decoration:none;
  background:rgba(0,0,0,.12)}
.widgets{position:absolute;left:0;top:522px;width:838px;height:382px;
  background:linear-gradient(180deg,#f2f2f2 0%,#e6e7e6 55%,#ededed 100%)}
.widget{position:absolute;width:238px;height:77px;border:3px solid var(--green-line);
  display:flex;align-items:center;justify-content:center;text-align:center;
  font-family:"Montserrat",sans-serif;font-weight:700;font-size:16px;line-height:22px;letter-spacing:1px;color:var(--green)}
.footer{position:absolute;left:0;top:904px;width:838px;height:296px;background:var(--green)}
.footer .brand{left:29px;top:28px}
.address{position:absolute;left:29px;top:126px;font-size:11px;line-height:17.8px;letter-spacing:.4px}
.copyright{position:absolute;left:29px;top:250px;font-size:11px;letter-spacing:.4px}
.badge{position:absolute;top:41px;height:55px;background:var(--white);border-radius:2px}
.badge.round{border-radius:50%/40%;background:#1b1b1b;border:2px solid var(--white)}
.social{position:absolute;top:221px;width:41px;height:40px;background:var(--white);border-radius:9px}
</style>
</head>
<body>
<header class="header">
  <div class="hero" role="img" aria-label="Slideshow photo: modern glass pavilion dining room looking out over the sea"></div>
  <svg class="hero-arrow prev" viewBox="0 0 16 28" aria-hidden="true"><polyline points="14,2 2,14 14,26" fill="none" stroke="#fff" stroke-width="1.5"/></svg>
  <svg class="hero-arrow next" viewBox="0 0 16 28" aria-hidden="true"><polyline points="2,2 14,14 2,26" fill="none" stroke="#fff" stroke-width="1.5"/></svg>
  <div class="brand"><span class="name"><span class="mark"></span>Brandt</span><span class="phone">270-555-3946</span></div>
  <div class="top-info">
    <span>5127 OLD HARROW LANE, SCOTTSVILLE, KY 42179</span>
    <span>TEL 270-555-3946</span>
    <span>FAX 270-555-3947</span>
    <span>EMAIL INFO@BRANDTPROPERTYBIDHOUSE.EXAMPLE</span>
  </div>
  <nav class="nav">
    <a href="#" style="left:161px">HOME</a>
    <a href="#" class="active">ALL AUCTIONS</a>
    <a href="#" style="left:327px">REAL ESTATE FOR SALE</a>
    <a href="#" style="left:480px">SERVICES</a>
    <a href="#" style="left:562px">ABOUT US</a>
    <a href="#" style="left:644px">CONTACT US</a>
  </nav>
  <div class="dropdown">
    <a href="#">UPCOMING AUCTIONS</a>
    <a href="#">ONLINE AUCTIONS</a>
    <a href="#">PAST AUCTIONS</a>
  </div>
</header>

<section class="widgets" role="img" aria-label="Faded grey background photo of a poolside patio">
  <div class="widget" style="left:30px;top:89px">EMAIL SIGNUP</div>
  <div class="widget" style="left:302px;top:89px">MESSAGE OF<br>THE DAY</div>
  <div class="widget" style="left:574px;top:89px">UPCOMING<br>AUCTIONS</div>
  <div class="widget" style="left:30px;top:216px">NEWS &amp; EVENTS<br>BLOG</div>
  <div class="widget" style="left:302px;top:216px">TESTIMONIALS</div>
  <div class="widget" style="left:574px;top:216px">SOCIAL MEDIA</div>
</section>

<footer class="footer">
  <div class="brand"><span class="name"><span class="mark"></span>Brandt</span><span class="phone">270-555-3946</span></div>
  <div class="address">
    5127 OLD HARROW LANE,<br>SCOTTSVILLE, KY 42179<br>TEL 270-555-3946<br>FAX 270-555-3947<br>EMAIL INFO@BRANDTPROPERTYBIDHOUSE.EXAMPLE
  </div>
  <div class="copyright">© 2015 BRANDT PROPERTY BID HOUSE</div>
  <div class="badge" style="left:464px;width:102px" role="img" aria-label="Auctioneer association badge"></div>
  <div class="badge round" style="left:588px;width:100px" role="img" aria-label="State auctioneers association badge"></div>
  <div class="badge" style="left:710px;width:102px" role="img" aria-label="Listing service badge"></div>
  <a class="social" href="#" style="left:525px" aria-label="Social link 1"></a>
  <a class="social" href="#" style="left:587px" aria-label="Social link 2"></a>
  <a class="social" href="#" style="left:648px" aria-label="Social link 3"></a>
  <a class="social" href="#" style="left:709px" aria-label="Social link 4"></a>
  <a class="social" href="#" style="left:770px" aria-label="Social link 5"></a>
</footer>
</body>
</html>
```